7 Reeds Distillery - Bottle Label Design

We are a small craft distillery whose branding needs to incorporate our location on a lake (Lac Vorbelle, Quebec, Canada). A unique aspect of the lake is that people drive floating docks on the lake powered by a small outboard motor (see photos). Back in the 1970’s when Lac Vorbelle was a sparsely populated and difficult-to-access lake in the Gatineau Hills north of Ottawa, the concept of motorized docks was conjured on a lazy afternoon and this single stroke of genius has inadvertently spawned the most exceptional and eccentric lake based community. Throughout the summer, somewhere around four o’clock on any given Friday and Saturday it starts to happen. Docks set sail from their customary landing places - family, friends, snacks and loaded drink coolers in-tow and, as if magnetically drawn, head toward Heron Shoal. Without fail they will come upon a gathering of similar minded floating docks within the vicinity - be guided in with help to moor alongside and within seconds be seamlessly immersed in the festivities. Seldom any longer are these events planned, they have become elemental, a thing organically derived from within the community. This on-going weekly event is the genesis of the strong bond that brings us Seven Reeds Distilling.
Each of the 4 distillery owners have one of these docks so hence the name. We are open to either "7 Reeds" or spelled out as "Seven Reeds" as may be visually appropriate. We are also open to "Distillery" or "Distilling". More detail on the docks themselves, they are 14x16 feet powered by a small outboard motor as shown in the photos. This dock aspect may be difficult to incorporate into the branding but the lake outline is included as an image applicable to include for that local reference aspect. We will be creating very high quality small batch liquors such as vodka, rum, gin and whiskey. Each batch will be triple distilled and perhaps 20 bottles in quantity so very exclusive. We are aiming at a premium feel for the branding. Attached are some bottle label designs that evoke the type of feel we are going for and a photo of the style of blank bottle to design for which is a 750ml Nordic pattern bottle.
In general we are going for more contemporary than traditional, more bold than delicate. If a single label the size desired would be 4 inches wide and 4 inches tall. If a double/split label as in two of the photos the top label would be 3 inches wide and 3 inches tall and the bottom label would be max 4 inches wide and 1.5 inches tall. We are open to the upper label being a "transparent" label to create a printed on bottle effect, perhaps of the brand logo. We are only interested in front label so do not require a back, neck or closure label. The label will require the ability to name the batch style name (example "Tuberov") and then the amplifying information for the type of alcohol (Russian Potato Vodka) in a smaller font. Another example ("Bell Cap" and "London Dry Gin"). Information for bottle size (750ml) and alcohol % (40%) are also to be included. Governmental safety warnings are not required. We are open to use of any colours in the label. The basic label design would be re-used for different types of batches where we would change the style and alcohol name.

Target Market(s)

Up scale premium spirits buyers

Font styles to use
Serif
Sans Serif

Requirements
Must have
• A visual reference to the docks or the lake per the images attached.
Nice to have
• Ideally we can re-use the label design for a different type of Alcohol by changing the alcohol name and style information and maybe the colour of a major element in the label.

```html
<!DOCTYPE html>
<html lang="en">
<head>
<meta charset="UTF-8">
<title>7 Reeds Distillery – Tuberov Label</title>
<link rel="stylesheet" href="https://fonts.googleapis.com/css2?family=Oswald:wght@400;500&family=Josefin+Sans:wght@400&display=swap">
<style>
  :root {
    --bg: #f6f6f4;
    --label: #eeede6;
    --label-light: #f7f7f1;
    --navy: #1b2e3f;
    --lake: #8bc4d6;
    --rule: #9aa3a8;
  }
  html, body {
    margin: 0;
    padding: 0;
    overflow: hidden;
  }
  .canvas {
    position: relative;
    width: 714px;
    height: 1200px;
    background: var(--bg);
    overflow: hidden;
  }
  .lake-print {
    position: absolute;
    left: 200px;
    top: 390px;
    width: 300px;
    height: 190px;
  }
  .label {
    position: absolute;
    left: 37px;
    top: 640px;
    width: 640px;
    height: 420px;
    background: linear-gradient(90deg, var(--label) 0%, var(--label-light) 50%, var(--label) 100%);
    box-sizing: border-box;
  }
  .brand {
    position: absolute;
    top: 70px;
    left: 0;
    right: 0;
    text-align: center;
    font-family: "Oswald", sans-serif;
    font-weight: 500;
    font-size: 70px;
    line-height: 1;
    letter-spacing: 1px;
    color: var(--navy);
    margin: 0;
  }
  .style-name {
    position: absolute;
    top: 262px;
    left: 0;
    right: 0;
    text-align: center;
    font-family: "Oswald", sans-serif;
    font-weight: 500;
    font-size: 38px;
    line-height: 1;
    color: var(--navy);
    text-transform: uppercase;
    margin: 0;
  }
  .spec-bar {
    position: absolute;
    left: 20px;
    right: 20px;
    top: 358px;
    height: 38px;
    border-top: 1px solid var(--rule);
    border-bottom: 1px solid var(--rule);
    display: flex;
    align-items: center;
    justify-content: space-between;
  }
  .spec {
    font-family: "Josefin Sans", sans-serif;
    font-size: 12px;
    letter-spacing: 1px;
    color: var(--navy);
    text-transform: uppercase;
  }
  .spirit-type {
    font-family: "Oswald", sans-serif;
    font-weight: 400;
    font-size: 19px;
    letter-spacing: 0.5px;
    color: var(--lake);
    text-transform: uppercase;
  }
</style>
</head>
<body>
  <main class="canvas">
    <svg class="lake-print" role="img" aria-label="Outline map of Lac Vorbelle" viewBox="0 0 300 190">
      <rect x="0" y="0" width="300" height="190" rx="40" fill="var(--lake)"/>
    </svg>

    <section class="label">
      <h1 class="brand">7 Reeds Distillery</h1>
      <h2 class="style-name">Tuberov</h2>
      <div class="spec-bar">
        <span class="spec spec-alcohol">Alc. 40%</span>
        <span class="spirit-type">Russian Potato Vodka</span>
        <span class="spec spec-volume">Vol. 750ml</span>
      </div>
    </section>
  </main>
</body>
</html>
```